PELDRAX Business Cards

We require a business card for our company that provides IT consulting services. We already have a logo that needs to be used on the card. We want a clean professional looking design that incorporates our colours. Our main focus is providing managed services to business, which involves us looking after all of their IT requirements including managing servers/networks, projects, and procurement.

Industry/Entity Type

Information Technology

Requirements
Must have
• our logo, contact information, name, title, phone numbers

```html
<!DOCTYPE html>
<html lang="en">
<head>
<meta charset="utf-8">
<title>PELDRAX Business Cards</title>
<link rel="stylesheet" href="https://fonts.googleapis.com/css2?family=Ubuntu:ital,wght@0,400;0,500;0,700;1,700&display=swap">
<style>
  :root {
    --brand-blue: #2996cf;
    --brand-blue-deep: #2189c2;
    --card-white: #ffffff;
    --stage: #3b2a21;
  }
  * { margin: 0; padding: 0; box-sizing: border-box; }
  html, body {
    width: 1200px;
    height: 1200px;
    overflow: hidden;
    background: var(--stage);
    font-family: "Ubuntu", sans-serif;
  }
  .canvas {
    position: relative;
    width: 1200px;
    height: 1200px;
  }
  .card {
    position: absolute;
    overflow: hidden;
  }
  .card-front {
    left: 218px;
    top: 131px;
    width: 752px;
    height: 429px;
    background: var(--brand-blue);
    display: flex;
    align-items: center;
    justify-content: center;
  }
  .front-wordmark {
    color: var(--card-white);
    font-weight: 500;
    font-size: 96px;
    letter-spacing: 6px;
    margin-top: -8px;
  }
  .card-back {
    left: 217px;
    top: 630px;
    width: 765px;
    height: 437px;
    background: var(--card-white);
  }
  .back-panel {
    position: absolute;
    left: 0;
    top: 0;
    width: 765px;
    height: 437px;
  }
  .back-panel .panel-main { fill: var(--brand-blue); }
  .back-panel .panel-shade { fill: var(--brand-blue-deep); }
  .holder {
    position: absolute;
    left: 48px;
    top: 164px;
    color: var(--card-white);
  }
  .holder-name {
    font-weight: 500;
    font-size: 47px;
    line-height: 1;
    letter-spacing: 0.5px;
  }
  .holder-title {
    font-size: 22px;
    margin-left: 8px;
    margin-top: 2px;
  }
  .back-wordmark {
    position: absolute;
    right: 35px;
    top: 38px;
    color: var(--brand-blue);
    font-weight: 500;
    font-size: 21px;
    letter-spacing: 1.5px;
  }
  .contact {
    position: absolute;
    left: 445px;
    top: 272px;
    color: var(--brand-blue);
  }
  .contact-label {
    font-weight: 700;
    font-style: italic;
    font-size: 27px;
    line-height: 1;
  }
  .contact-value {
    font-size: 20px;
    line-height: 1.1;
    margin-bottom: 12px;
  }
</style>
</head>
<body>
  <main class="canvas">
    <section class="card card-front">
      <div class="front-wordmark">PELDRAX</div>
    </section>

    <section class="card card-back">
      <svg class="back-panel" viewBox="0 0 765 437" aria-hidden="true">
        <path class="panel-main" d="M0 0 H302 Q385 38 456 71 Q448 300 281 437 H0 Z"/>
        <path class="panel-shade" d="M456 71 Q448 300 281 437 H240 Q430 300 456 71 Z"/>
      </svg>

      <div class="back-wordmark">PELDRAX</div>

      <div class="holder">
        <div class="holder-name">YOUR NAME</div>
        <div class="holder-title">job title</div>
      </div>

      <div class="contact">
        <div class="contact-label">email.</div>
        <div class="contact-value">youremail@yourdomain.com</div>
        <div class="contact-label">phone.</div>
        <div class="contact-value">123.456.7891</div>
      </div>
    </section>
  </main>
</body>
</html>
```